Website for Marlow Crest Telecom

I need a website done for Marlow Crest Telecom, a new telecommunications business launching in Australia which provides the best internet connectivity for Businesses. It needs to start with the home page, including the logo, layout, colour, font. The rest of the website will follow, around 12 pages.

Ideally the logo will be maximum two colours, with the words Marlow Crest Telecom being the logo rather than another symbol. The emphasis needs to be on the word Marlow. The design needs to be simple and minimal. I am not sure yet whether the designer will code the page or I will get someone else to do it.

The colours on the slide attached are not meant to be the colours to use, but the layout is close to what I envisage.

```html
<!DOCTYPE html>
<html lang="en">
<head>
<meta charset="utf-8">
<title>Marlow Crest Telecom — Business Internet</title>
<link href="https://fonts.googleapis.com/css2?family=Poppins:wght@300;400;500;600;700&display=swap" rel="stylesheet">
<style>
:root{
  --navy:#14137d;
  --blue:#2f9cf2;
  --blue-soft:#dbeeff;
  --ink:#333;
  --muted:#6b6b6b;
  --grey-bg:#f5f5f5;
  --icon-bg:#f0f0f2;
  --white:#fff;
}
*{box-sizing:border-box;margin:0;padding:0}
html,body{width:1200px;height:3437px;overflow:hidden}
body{font-family:'Poppins',sans-serif;color:var(--ink);background:var(--white);position:relative}
a{color:inherit;text-decoration:none}

/* top bar */
.topbar{position:absolute;top:0;left:0;width:1200px;height:37px;background:var(--navy);color:var(--white);display:flex;justify-content:flex-end;align-items:center;gap:26px;padding-right:60px;font-size:14px}
.topbar span{display:flex;align-items:center;gap:8px}
.topbar .phone{font-weight:600}

/* brand wordmark: one colour, one weight, Marlow emphasised by size */
.brand{color:var(--navy);font-weight:600;white-space:nowrap}
.brand .brand-lead{display:block;font-size:25px;line-height:27px;letter-spacing:1px}
.brand .brand-tail{display:block;font-size:18px;line-height:22px}

/* nav */
.nav{position:absolute;top:37px;left:0;width:1200px;height:64px;display:flex;align-items:center;justify-content:space-between;padding:0 60px 0 61px}
.nav ul{list-style:none;display:flex;gap:40px;font-size:14px;font-weight:500;color:#222}

/* hero */
.hero{position:absolute;top:101px;left:0;width:1200px;height:562px}
.hero-bg{position:absolute;inset:0;background:radial-gradient(ellipse at 78% 45%,#3f8fd6 0%,#1b4f7e 25%,#21303f 55%,#1c2128 100%)}
.hero-copy{position:absolute;left:61px;top:144px;width:520px;color:var(--white)}
.hero-copy h1{font-size:36px;font-weight:600;line-height:45px;white-space:nowrap}
.hero-copy h1 em{font-style:normal;color:var(--blue)}
.hero-copy p{margin-top:30px;width:440px;font-size:14px;line-height:22.5px;font-weight:400}
.btn{display:inline-flex;align-items:center;justify-content:center;background:var(--navy);color:var(--white);border:2px solid #3d3dc9;border-radius:20px;font-size:13px;text-transform:uppercase;white-space:nowrap}
.hero .btn{margin-top:46px;width:116px;height:36px}

/* section titles */
.sec-title{position:absolute;left:0;width:1200px;text-align:center;font-size:28px;font-weight:600;color:var(--navy)}
.sec-title em{font-style:normal;color:var(--blue)}
.sec-sub{position:absolute;left:0;width:1200px;text-align:center;font-size:14px;line-height:20px;color:var(--muted)}

/* why choose */
.deco-disc{position:absolute;left:-18px;top:683px;width:114px;height:114px;border-radius:50%;background:var(--blue-soft)}
.deco-ring{position:absolute;left:1130px;top:1315px;width:100px;height:96px;border-radius:50%;border:2px solid var(--blue)}
.features{position:absolute;left:48px;top:849px;width:1108px;display:grid;grid-template-columns:repeat(4,277px);grid-template-rows:263px 240px}
.feature{text-align:center;position:relative}
.feature .ic{width:86px;height:86px;border-radius:50%;background:var(--icon-bg);margin:0 auto;display:flex;align-items:center;justify-content:center}
.feature .ic.active{background:var(--navy);box-shadow:0 0 0 3px var(--white),0 0 0 4px var(--blue)}
.feature h3{margin-top:14px;font-size:13px;font-weight:600;color:var(--navy);text-transform:uppercase}
.feature p{margin:4px auto 0;width:205px;font-size:14.5px;line-height:22.5px;color:#444}
.feature .more{position:absolute;left:0;right:0;top:208px;font-size:14px;color:var(--blue);display:flex;justify-content:center;align-items:center;gap:4px}

/* about */
.about{position:absolute;top:1415px;left:0;width:1200px;height:438px;background:var(--grey-bg)}
.about-frame{position:absolute;left:45px;top:37px;width:546px;height:334px;border:1px solid #8fc3f2;border-radius:8px}
.about-photo{position:absolute;left:60px;top:53px;width:517px;height:330px;background:linear-gradient(135deg,#6a5a4a 0%,#b8b1a6 40%,#5b6a7e 70%,#2f2a26 100%)}
.badge{position:absolute;left:506px;top:40px;width:104px;height:104px;border-radius:50%;background:var(--navy);border:3px solid var(--white);color:var(--white);text-align:center;display:flex;flex-direction:column;justify-content:center;font-size:14px;line-height:17px;font-weight:500}
.badge b{font-size:17px;font-weight:600}
.about-copy{position:absolute;left:657px;top:54px;width:490px}
.eyebrow{font-size:14px;color:var(--blue);font-weight:500}
.about-copy h2{font-size:28px;font-weight:600;color:var(--navy);margin-top:6px}
.about-copy p{margin-top:12px;font-size:12px;line-height:22.5px;color:#555}
.about-copy ul{list-style:none;margin-top:20px;margin-left:-6px}
.about-copy li{display:flex;gap:8px;font-size:12.5px;line-height:22.5px;color:var(--navy);margin-bottom:9px}
.about-copy li svg{flex:none;margin-top:3px}

/* news */
.cards{position:absolute;left:60px;top:2039px;width:1080px;display:flex;justify-content:space-between}
.card{width:339px}
.card-img{height:187px;border-radius:10px}
.card h3{margin-top:17px;font-size:17px;font-weight:600;color:var(--navy);padding-left:2px;white-space:nowrap}
.card p{margin-top:8px;font-size:14px;line-height:22.5px;color:var(--muted);padding-left:2px}
.card .more{margin-top:6px;font-size:13px;color:var(--blue);display:flex;align-items:center;gap:8px;padding-left:2px}
.news-btn{position:absolute;left:527px;top:2437px;width:146px;height:34px}

/* partners */
.partners{position:absolute;top:2552px;left:0;width:1200px;height:278px;background:var(--blue)}
.partners h2{position:absolute;top:54px;width:1200px;text-align:center;font-size:28px;font-weight:500;color:var(--white)}
.partner-row{position:absolute;top:140px;left:60px;width:1080px;display:flex;justify-content:space-between;align-items:center}
.partner{display:flex;align-items:center;gap:8px;color:var(--white);font-size:40px;font-weight:400;letter-spacing:-0.5px;white-space:nowrap}
.partner i{display:block;width:44px;height:44px;border-radius:50%;background:rgba(255,255,255,.35)}
.arrow-l,.arrow-r{position:absolute;top:136px}
.arrow-l{left:16px}.arrow-r{left:1160px}

/* contact */
.search{position:absolute;left:334px;top:2993px;width:532px;height:40px;border:1px solid #999;border-radius:20px;display:flex;align-items:center;justify-content:space-between;padding:0 2px 0 15px;font-size:13px;color:#444}
.search .btn{width:102px;height:34px;border:none;border-radius:17px;font-size:13px}
.chat{position:absolute;left:1021px;top:3062px;display:flex;align-items:center;gap:12px}
.chat .bubble{width:46px;height:46px;border-radius:50%;background:var(--navy);display:flex;align-items:center;justify-content:center;box-shadow:0 2px 8px rgba(0,0,0,.25)}
.chat .label{background:var(--white);box-shadow:0 2px 10px rgba(0,0,0,.12);border-radius:20px;padding:10px 18px;font-size:13px;color:#333}

/* footer */
.footer{position:absolute;top:3114px;left:0;width:1200px;height:323px;background:var(--navy);color:var(--white)}
.footer .brand{position:absolute;left:509px;top:56px;color:var(--white)}
.footer .brand .brand-lead{font-size:27px;line-height:31px}
.footer .brand .brand-tail{font-size:22px;line-height:28px}
.footer-links{position:absolute;top:137px;left:0;width:1200px;display:flex;justify-content:center;list-style:none;font-size:13px}
.footer-links li{padding:0 18px;border-left:1px solid var(--blue)}
.footer-links li:first-child{border-left:none}
.f-col{position:absolute;top:178px;text-align:center;font-size:12.5px;line-height:24px;white-space:nowrap}
.f-col .ring{width:40px;height:40px;border:1.5px solid var(--blue);border-radius:50%;margin:0 auto 12px;display:flex;align-items:center;justify-content:center}
.f-col b{font-weight:600}
.footer-rule{position:absolute;top:288px;left:0;width:1200px;height:1px;background:#3b3ba0}
.copy{position:absolute;top:296px;width:1200px;text-align:center;font-size:12px}
.copy em{font-style:normal;color:var(--blue)}
</style>
</head>
<body>
<svg width="0" height="0" style="position:absolute">
  <defs>
    <symbol id="go" viewBox="0 0 26 14"><circle cx="7" cy="7" r="6" fill="none" stroke="currentColor" stroke-width="1.2"/><path d="M4 7h20M19 2.5 24 7l-5 4.5" fill="none" stroke="currentColor" stroke-width="1.2"/></symbol>
    <symbol id="phone" viewBox="0 0 24 24"><path d="M6.6 3.5 9 3l1.6 4.3-2 1.3a11 11 0 0 0 6.8 6.8l1.3-2L21 15l-.5 2.4A3 3 0 0 1 17.5 20 14.5 14.5 0 0 1 4 6.5a3 3 0 0 1 2.6-3z" fill="none" stroke="currentColor" stroke-width="1.4" stroke-linejoin="round"/></symbol>
    <symbol id="mail" viewBox="0 0 24 24"><rect x="2.5" y="5" width="19" height="14" rx="1.5" fill="none" stroke="currentColor" stroke-width="1.4"/><path d="m3 6 9 7 9-7" fill="none" stroke="currentColor" stroke-width="1.4"/></symbol>
    <symbol id="pin" viewBox="0 0 24 24"><path d="M12 21s-6.5-6.6-6.5-11.3a6.5 6.5 0 0 1 13 0C18.5 14.4 12 21 12 21z" fill="none" stroke="currentColor" stroke-width="1.4"/><circle cx="12" cy="9.7" r="2.4" fill="none" stroke="currentColor" stroke-width="1.4"/></symbol>
  </defs>
</svg>

<header class="topbar">
  <span class="phone"><svg width="18" height="18"><use href="#phone"/></svg>1300 XXX XXX</span>
  <span><svg width="20" height="20"><use href="#mail"/></svg>sales@marlowcresttelecom.com.au</span>
  <span><svg width="20" height="20"><use href="#mail"/></svg>support@marlowcresttelecom.com.au</span>
</header>

<nav class="nav">
  <div class="brand"><span class="brand-lead">MARLOW</span><span class="brand-tail">Crest Telecom</span></div>
  <ul><li>Products</li><li>About</li><li>News &amp; Insights</li><li>Partners</li><li>Contact</li></ul>
</nav>

<section class="hero">
  <div class="hero-bg" role="img" aria-label="Hand holding a glowing network of floating app and connectivity icons on a dark blurred city background"></div>
  <div class="hero-copy">
    <h1>A New From <em>Telecommuni-</em><br><em>cations Business</em></h1>
    <p>Corelink Enterprise Ethernet provides businesses of all sizes with superfast, affordable internet over a dedicated fibre – which means it never slows down during peak periods.</p>
    <a class="btn">Read More</a>
  </div>
</section>

<div class="deco-disc"></div>
<h2 class="sec-title" style="top:740px">Why <em>Choose Us</em></h2>
<p class="sec-sub" style="top:780px">Lorem Ipsum is simply dummy text of the printing<br>and typesetting industry.</p>

<section class="features">
  <div class="feature">
    <div class="ic"><svg width="50" height="40" viewBox="0 0 50 40" fill="none" stroke="#14137d" stroke-width="1.6"><path d="M18 30h22a8 8 0 0 0 0-16 11 11 0 0 0-21-2 8 8 0 0 0-1 18z"/><path d="M2 16h12M5 21h9M2 26h12M6 31h9" stroke="#2f9cf2"/></svg></div>
    <h3>Fast</h3><p style="width:165px">From 100Mbps up to 1Gbps* speed options</p>
    <a class="more">Learn More <svg width="26" height="14"><use href="#go"/></svg></a>
  </div>
  <div class="feature">
    <div class="ic active"><svg width="40" height="46" viewBox="0 0 40 46" fill="none" stroke="#fff" stroke-width="1.8"><path d="M8 44V30h24v14M14 30V22h12v8M16 22V6M20 22V3M24 22V6M13 12l3-2M27 12l-3-2"/></svg></div>
    <h3>Dedicated Fibre</h3><p style="width:170px">doesn't slow down with multiple concurrent users</p>
    <a class="more">Learn More <svg width="26" height="14"><use href="#go"/></svg></a>
  </div>
  <div class="feature">
    <div class="ic"><svg width="46" height="46" viewBox="0 0 46 46" fill="none" stroke="#14137d" stroke-width="1.6"><path d="M13 20h20a6 6 0 0 0 0-12 9 9 0 0 0-17-1 6 6 0 0 0-3 13z"/><rect x="12" y="24" width="22" height="6" rx="1"/><rect x="12" y="32" width="22" height="6" rx="1"/><path d="M4 42h38" stroke="#2f9cf2"/></svg></div>
    <h3>Symmetric</h3><p style="width:175px">same download and upload speeds, critical for business use</p>
    <a class="more">Learn More <svg width="26" height="14"><use href="#go"/></svg></a>
  </div>
  <div class="feature">
    <div class="ic"><svg width="46" height="46" viewBox="0 0 46 46" fill="none" stroke="#14137d" stroke-width="1.6"><circle cx="23" cy="23" r="15"/><ellipse cx="23" cy="23" rx="6.5" ry="15"/><path d="M8 23h30M10 15h26M10 31h26"/><circle cx="23" cy="23" r="20" stroke="#2f9cf2" stroke-dasharray="3 4"/></svg></div>
    <h3>Widely Available</h3><p style="width:220px">1.5M sites around Australia including metro, regional and remote locations</p>
    <a class="more">Learn More <svg width="26" height="14"><use href="#go"/></svg></a>
  </div>
  <div class="feature">
    <div class="ic"><svg width="50" height="46" viewBox="0 0 50 46" fill="none" stroke="#14137d" stroke-width="1.6"><circle cx="20" cy="22" r="15"/><ellipse cx="20" cy="22" rx="6" ry="15"/><path d="M5 22h30M7 14h26M7 30h26"/><path d="M32 22l9-3 7 3v8c0 6-7 10-7 10s-7-4-7-10z" fill="#fff" stroke="#2f9cf2"/><path d="m37 29 3 3 5-6" stroke="#2f9cf2"/></svg></div>
    <h3>Reliable</h3><p style="width:205px">Designed for up to 99.95% network availability with 4G back up option</p>
    <a class="more">Learn More <svg width="26" height="14"><use href="#go"/></svg></a>
  </div>
  <div class="feature">
    <div class="ic"><svg width="52" height="40" viewBox="0 0 52 40" fill="none" stroke="#14137d" stroke-width="1.5"><circle cx="12" cy="22" r="4"/><circle cx="26" cy="22" r="4"/><circle cx="40" cy="22" r="4"/><path d="M5 34a7 7 0 0 1 14 0M19 34a7 7 0 0 1 14 0M33 34a7 7 0 0 1 14 0M3 36h46"/><path d="m12 4 1.5 3 3 .5-2.2 2 .6 3L12 11l-2.9 1.5.6-3-2.2-2 3-.5zM26 4l1.5 3 3 .5-2.2 2 .6 3L26 11l-2.9 1.5.6-3-2.2-2 3-.5zM40 4l1.5 3 3 .5-2.2 2 .6 3L40 11l-2.9 1.5.6-3-2.2-2 3-.5z" stroke="#2f9cf2"/></svg></div>
    <h3>Expert Support</h3><p style="width:160px">100% Australian team with 24x7 service</p>
    <a class="more">Learn More <svg width="26" height="14"><use href="#go"/></svg></a>
  </div>
  <div class="feature">
    <div class="ic"><svg width="46" height="46" viewBox="0 0 46 46" fill="none" stroke="#14137d" stroke-width="1.6"><rect x="12" y="10" width="24" height="30" rx="1.5"/><path d="M17 24h14M17 29h14M17 34h10"/><circle cx="16" cy="12" r="7" fill="#fff" stroke="#2f9cf2"/><path d="M21 17l5 5" stroke="#2f9cf2"/><path d="m30 14 8-8 3 3-8 8-4 1z"/></svg></div>
    <h3>No Upfront Build Cost</h3><p style="width:150px">in 90% of cases on a standard 3 year contract**</p>
    <a class="more">Learn More <svg width="26" height="14"><use href="#go"/></svg></a>
  </div>
  <div class="feature">
    <div class="ic"><svg width="46" height="46" viewBox="0 0 46 46" fill="none" stroke="#14137d" stroke-width="1.6"><path d="M6 20l8-6h8l10-6 4 4-10 7M40 26l-8 6h-8l-10 6-4-4 10-7"/><circle cx="23" cy="23" r="5" stroke="#2f9cf2"/><path d="M23 20v6" stroke="#2f9cf2"/></svg></div>
    <h3>Affordable</h3><p style="width:140px">starting at $X per month</p>
    <a class="more">Learn More <svg width="26" height="14"><use href="#go"/></svg></a>
  </div>
</section>
<div class="deco-ring"></div>

<section class="about">
  <div class="about-frame"></div>
  <div class="about-photo" role="img" aria-label="Person browsing a smartphone at a wooden desk beside a coffee cup and laptop"></div>
  <div class="badge"><span>Up To</span><b>55 MB</b><span>Per Second</span></div>
  <div class="about-copy">
    <div class="eyebrow">About Us</div>
    <h2>What Who We Are</h2>
    <p>Lorem Ipsum is simply dummy text of the printing and typesetting industry. Lorem Ipsum has been the industry's standard dummy text ever since the 1500s, when an unknown printer took a galley of type and scrambled it to make a type specimen book. It has survived not only five centuries.</p>
    <ul>
      <li><svg width="26" height="14" style="color:#2f9cf2"><use href="#go"/></svg>Actual speed capped at 952Mbps and may vary due to various equipment and network factors</li>
      <li><svg width="26" height="14" style="color:#2f9cf2"><use href="#go"/></svg>Other contract term options available, however No upfront build starts on 3 year contract</li>
    </ul>
  </div>
</section>

<h2 class="sec-title" style="top:1931px">News &amp; <em>Insights</em></h2>
<p class="sec-sub" style="top:1971px">Lorem Ipsum is simply dummy text of the printing<br>and typesetting industry.</p>

<section class="cards">
  <article class="card">
    <div class="card-img" role="img" aria-label="Satellite dish against a blurred evening city skyline" style="background:linear-gradient(160deg,#5b86c4 0%,#9fb9dc 50%,#d8dde6 100%)"></div>
    <h3>Lorem Ipsum is simply dummy text</h3>
    <p>Lorem Ipsum is simply dummy text of the printing and typesetting industry. Lorem Ipsum has been the industry's standard dummy text ever since the 1500s, when an unknown printer.</p>
    <a class="more">READ MORE <svg width="26" height="14"><use href="#go"/></svg></a>
  </article>
  <article class="card">
    <div class="card-img" role="img" aria-label="Woman using a phone under a glass dome roof" style="background:linear-gradient(170deg,#5d7fa0 0%,#a7b9c8 55%,#7b8590 100%)"></div>
    <h3>Lorem Ipsum is simply dummy text</h3>
    <p>Lorem Ipsum is simply dummy text of the printing and typesetting industry. Lorem Ipsum has been the industry's standard dummy text ever since the 1500s, when an unknown printer.</p>
    <a class="more">READ MORE <svg width="26" height="14"><use href="#go"/></svg></a>
  </article>
  <article class="card">
    <div class="card-img" role="img" aria-label="Telecommunication towers seen from below against a pale blue sky" style="background:linear-gradient(180deg,#8fb2d8 0%,#c6d8ec 60%,#e6eef7 100%)"></div>
    <h3>Lorem Ipsum is simply dummy text</h3>
    <p>Lorem Ipsum is simply dummy text of the printing and typesetting industry. Lorem Ipsum has been the industry's standard dummy text ever since the 1500s, when an unknown printer.</p>
    <a class="more">READ MORE <svg width="26" height="14"><use href="#go"/></svg></a>
  </article>
</section>
<a class="btn news-btn">See More Posts</a>

<section class="partners">
  <h2>Our Partners</h2>
  <svg class="arrow-l" width="22" height="30" viewBox="0 0 22 30"><path d="M15 6 7 15l8 9" fill="none" stroke="#fff" stroke-width="3"/></svg>
  <div class="partner-row">
    <span class="partner"><i></i>Norvale</span>
    <span class="partner"><i></i>Orbitra</span>
    <span class="partner"><i></i>Kestra</span>
    <span class="partner"><i></i>Lumio</span>
    <span class="partner"><i></i>Tessan</span>
  </div>
  <svg class="arrow-r" width="22" height="30" viewBox="0 0 22 30"><path d="m7 6 8 9-8 9" fill="none" stroke="#fff" stroke-width="3"/></svg>
</section>

<h2 class="sec-title" style="top:2893px">Contact <em>Us</em></h2>
<p class="sec-sub" style="top:2932px">Lorem Ipsum is simply dummy text of the printing<br>and typesetting industry.</p>
<form class="search"><span>Address (number, street, suburb, state, postcode)</span><span class="btn">Search</span></form>
<div class="chat">
  <span class="bubble"><svg width="26" height="24" viewBox="0 0 26 24"><path d="M13 2C6.9 2 2 6 2 11c0 2.6 1.3 4.9 3.5 6.5L4.5 22l5-2.5c1.1.3 2.3.5 3.5.5 6.1 0 11-4 11-9S19.1 2 13 2z" fill="#fff"/><circle cx="8.5" cy="11" r="1.5" fill="#14137d"/><circle cx="13" cy="11" r="1.5" fill="#14137d"/><circle cx="17.5" cy="11" r="1.5" fill="#14137d"/></svg></span>
  <span class="label">LIVE CHAT</span>
</div>

<footer class="footer">
  <div class="brand"><span class="brand-lead">MARLOW</span><span class="brand-tail">Crest Telecom</span></div>
  <ul class="footer-links"><li>Products</li><li>About</li><li>News &amp; Insights</li><li>Partners</li><li>Contact</li></ul>
  <div class="f-col" style="left:278px;width:220px"><div class="ring"><svg width="22" height="22"><use href="#pin"/></svg></div>123 ,lorem ipsum dummy text.<br>123 ,lorem ipsum dummy text.</div>
  <div class="f-col" style="left:510px;width:130px;top:184px"><div class="ring"><svg width="20" height="20"><use href="#phone"/></svg></div><b>1300 XXX XXX</b></div>
  <div class="f-col" style="left:662px;width:250px;top:182px"><div class="ring"><svg width="22" height="22"><use href="#mail"/></svg></div>sales@marlowcresttelecom.com.au<br>support@marlowcresttelecom.com.au</div>
  <div class="footer-rule"></div>
  <p class="copy">© 2022 <em>Marlow Crest Telecom</em>. All rights reserved.</p>
</footer>
</body>
</html>
```